Create Brisk Lesson Studio a card design that will stick in the mind of prospects.

Brisk Lesson Studio specialises designs and produces training video, animation, illustration and text.

We need a card design that oozes class and leaves the prospect brimming with confidence.

The design will feature the Brisk Lesson Studio all black logo (uploaded). The design may also use the shade of orange from the orange version of the logo (uploaded). Note, just the color is to be used e.g. for the back of the card, not the orange logo itself.

The Brisk brand is about authenticity, quality, maturity and assurance. We are a safe buy when it comes to the prospects next project.

Target Market(s)

The primary target is training managers or others who are responsible for choosing to hire companies to produce their training media e.g. video. This will usually be a large spend so they need to have confidence.

Industry/Entity Type

Training

Contact Information for Business Card

FRONT:

Brisk Lesson Studio
Phone: 03 5172 4039
1st Floor, 418 Kellerby Road
Mt Ferncombe
VIC 3862
Australia
www.brisklesson.com.au

Lionel Petch
Founder and Lead Consultant
mobile: +61 3 0462 735 218
email: lionel@brisklesson.com.au

BACK:
Specialising in design and production of training:

video
animation
illustration
text

for delivery via internet, intranet and/or LMS.

Number of Pages Required

4 page

Font styles to use
Sans Serif

Requirements
Must have
• The black logo uploaded with the brief.
Nice to have
• The inclusion of the shade of orange found in the orange logo also uploaded with the brief. One example would be having the back of the card in this orange and using a white font for the text. But I want the designer to work this out.
Should not have
• No colours other than black and the orange included in the uploaded orange logo.

```html
<!DOCTYPE html>
<html lang="en">
<head>
<meta charset="utf-8">
<title>Brisk Lesson Studio — Business Cards</title>
<link rel="stylesheet" href="https://fonts.googleapis.com/css2?family=Barlow:wght@400;500;600&display=swap">
<style>
  :root {
    --page: #ffffff;
    --card: #fdf5ec;
    --orange: #e05434;
    --grey: #8a847e;
    --shadow: rgba(0, 0, 0, 0.18);
  }
  * { margin: 0; padding: 0; box-sizing: border-box; }
  html, body {
    width: 1200px; height: 1200px; overflow: hidden;
    background: var(--page);
    font-family: "Barlow", sans-serif;
  }
  .sheet { position: relative; width: 1200px; height: 1200px; }
  .card {
    position: absolute;
    width: 267px; height: 467px;
    background: var(--card);
    box-shadow: 6px 6px 6px var(--shadow);
  }
  .card--front-light { left: 304px; top: 96px; }
  .card--back-top    { left: 630px; top: 96px; }
  .card--front-orange { left: 302px; top: 642px; width: 269px; height: 471px; background: var(--orange); }
  .card--back-bottom { left: 630px; top: 642px; width: 268px; height: 471px; }

  .wordmark {
    position: absolute; left: 0; right: 0; top: 166px;
    display: flex; align-items: center; justify-content: center; gap: 8px;
    font-weight: 600; font-size: 22px; letter-spacing: 0.02em;
    color: var(--orange);
  }
  .wordmark__dot {
    width: 12px; height: 12px; border-radius: 50%;
    background: var(--orange);
  }
  .card--front-orange .wordmark { color: #ffffff; top: 168px; }
  .card--front-orange .wordmark__dot { background: #ffffff; }

  .contact { position: absolute; left: 26px; right: 10px; top: 0; bottom: 0; }
  .contact__name {
    position: absolute; top: 42px;
    font-weight: 600; font-size: 17px; color: var(--orange); letter-spacing: 0.01em;
  }
  .contact__role {
    position: absolute; top: 62px;
    font-size: 13.5px; color: var(--grey); letter-spacing: 0.03em;
  }
  .contact__details {
    position: absolute; top: 247px;
    font-size: 13.5px; line-height: 17.4px; color: var(--grey); letter-spacing: 0.03em;
    list-style: none;
  }
  .contact__rule { color: var(--orange); }
  .contact__web {
    position: absolute; top: 413px;
    font-weight: 500; font-size: 13.5px; color: var(--orange); letter-spacing: 0.02em;
  }
</style>
</head>
<body>
<main class="sheet">
  <section class="card card--front-light">
    <div class="wordmark"><span class="wordmark__dot"></span>Brisk Lesson Studio</div>
  </section>

  <section class="card card--back-top">
    <div class="contact">
      <p class="contact__name">Lionel Petch</p>
      <p class="contact__role">Founder and Lead Consultant</p>
      <ul class="contact__details">
        <li>Brisk Lesson Studio</li>
        <li>1st Floor, 418 Kellerby Road</li>
        <li>Mt Ferncombe</li>
        <li>VIC 3862</li>
        <li>Australia</li>
        <li class="contact__rule">–</li>
        <li>P:&nbsp; +03 5172 4039</li>
        <li>M: +61 3 0462 735 218</li>
        <li>lionel@brisklesson.com.au</li>
      </ul>
      <p class="contact__web">www.brisklesson.com.au</p>
    </div>
  </section>

  <section class="card card--front-orange">
    <div class="wordmark"><span class="wordmark__dot"></span>Brisk Lesson Studio</div>
  </section>

  <section class="card card--back-bottom">
    <div class="contact">
      <p class="contact__name">Lionel Petch</p>
      <p class="contact__role">Founder and Lead Consultant</p>
      <ul class="contact__details">
        <li>Brisk Lesson Studio</li>
        <li>1st Floor, 418 Kellerby Road</li>
        <li>Mt Ferncombe</li>
        <li>VIC 3862</li>
        <li>Australia</li>
        <li class="contact__rule">–</li>
        <li>P:&nbsp; +03 5172 4039</li>
        <li>M: +61 3 0462 735 218</li>
        <li>lionel@brisklesson.com.au</li>
      </ul>
      <p class="contact__web">www.brisklesson.com.au</p>
    </div>
  </section>
</main>
</body>
</html>
```